Package for a Mouthfreshener called ZOLV!!

We are looking for an awesome packaging design for a bran new product called “Zolv Mouthfreshener”

This product is going to be made in USA so is really importar that ‘Made in USA” is part of the packaging.

We also need to include the ingredients that are going to be the following:
Saffron
cardamom
menthol
catechu
permited spices and falvors
tree nuts.

We are looking to haver this in a green or purple color and to clarify that the “best before” is for 2 years after the production date

Target Market(s)

Indian stores in usa

Colors
0094D4
00A9DD
6FCCEA
C7EBF8
E9F6FB
00AB8E
00BBA5
67D7C9
C6EFE9
E9F9F6
6B429C
8869AF
B7A5CE
E3DAEB
F3F0F8

Requirements
Must have
• Ingredients
Nice to have
• A good font and is important to mention is made in USA on images I upload an idea for the font

```html
<!DOCTYPE html>
<html lang="en">
<head>
<meta charset="utf-8">
<title>Zolv Mouthfreshener – Pouch Front</title>
<link href="https://fonts.googleapis.com/css2?family=Abril+Fatface&family=Open+Sans:wght@400;500;600&family=Luckiest+Guy&display=swap" rel="stylesheet">
<style>
  :root {
    --backdrop: #e6d3a6;
    --purple-deep: #4a1f6e;
    --purple: #6b429c;
    --purple-mid: #8869af;
    --purple-light: #b7a5ce;
    --label-white: #f4f2f1;
    --ink: #1a1414;
    --red: #e2322d;
    --orange: #f07a35;
  }
  html, body {
    margin: 0;
    padding: 0;
    width: 1133px;
    height: 1200px;
    overflow: hidden;
    background: var(--backdrop);
  }
  .canvas {
    position: relative;
    width: 1133px;
    height: 1200px;
  }
  .pouch {
    position: absolute;
    left: 246px;
    top: 70px;
    width: 640px;
    height: 1060px;
  }
  .pouch-art {
    position: absolute;
    inset: 0;
  }
  .label-text {
    position: absolute;
    left: 80px;
    width: 480px;
    text-align: center;
    margin: 0;
  }
  .brand-name {
    top: 168px;
    font-family: "Abril Fatface", serif;
    font-size: 110px;
    font-weight: 400;
    line-height: 1;
    color: var(--ink);
    letter-spacing: 1px;
  }
  .product-name {
    top: 290px;
    font-family: "Open Sans", sans-serif;
    font-weight: 500;
    font-size: 50px;
    line-height: 1;
    color: var(--ink);
  }
  .origin {
    top: 362px;
    font-family: "Luckiest Guy", sans-serif;
    color: var(--red);
    line-height: 1;
  }
  .origin .small { font-size: 40px; }
  .origin .big { font-size: 64px; }
  .ingredients {
    top: 486px;
    font-family: "Open Sans", sans-serif;
    font-size: 19px;
    line-height: 1.35;
    color: var(--ink);
    letter-spacing: 0.5px;
    text-transform: uppercase;
  }
  .ingredients .pair span { margin: 0 14px; }
  .net-weight {
    top: 606px;
    font-family: "Open Sans", sans-serif;
    font-size: 19px;
    line-height: 1.35;
    color: var(--ink);
  }
</style>
</head>
<body>
<main class="canvas">
  <section class="pouch">
    <svg class="pouch-art" width="640" height="1060" viewBox="0 0 640 1060">
      <defs>
        <linearGradient id="patternTone" x1="0" y1="0" x2="1" y2="1">
          <stop offset="0" stop-color="#5a2a85"/>
          <stop offset="0.5" stop-color="#7a4aa8"/>
          <stop offset="1" stop-color="#4f2276"/>
        </linearGradient>
        <radialGradient id="spiceTone" cx="0.5" cy="0.5" r="0.5">
          <stop offset="0" stop-color="#d49a4a"/>
          <stop offset="0.6" stop-color="#9a5a2c"/>
          <stop offset="1" stop-color="#6a3520"/>
        </radialGradient>
        <path id="badgeArc" d="M208,810 A112,112 0 0 1 432,810"/>
      </defs>

      <rect class="pouch-pattern" x="0" y="0" width="640" height="1060" rx="6"
            fill="url(#patternTone)" role="img"
            aria-label="Purple floral mandala pattern with orange and pink blossoms"/>

      <path class="label-panel"
            d="M80,200 Q80,170 110,165 Q160,160 200,130 Q260,90 320,90 Q380,90 440,130 Q480,160 530,165 Q560,170 560,200 L560,880 Q560,910 530,915 Q480,920 440,950 Q380,990 320,990 Q260,990 200,950 Q160,920 110,915 Q80,910 80,880 Z"
            fill="var(--label-white)" stroke="var(--purple-deep)" stroke-width="4"/>
      <path class="label-frame"
            d="M96,212 Q96,185 122,181 Q170,176 210,146 Q266,106 320,106 Q374,106 430,146 Q470,176 518,181 Q544,185 544,212 L544,868 Q544,895 518,899 Q470,904 430,934 Q374,974 320,974 Q266,974 210,934 Q170,904 122,899 Q96,895 96,868 Z"
            fill="none" stroke="var(--purple)" stroke-width="2"/>

      <line class="divider" x1="130" y1="470" x2="510" y2="470"
            stroke="var(--ink)" stroke-width="1.5" stroke-dasharray="7 6"/>

      <circle class="spice-photo" cx="320" cy="810" r="92" fill="url(#spiceTone)"
              role="img" aria-label="Photo of colourful mouth freshener spice mix"/>
      <circle cx="202" cy="835" r="4" fill="var(--red)"/>
      <circle cx="438" cy="835" r="4" fill="var(--red)"/>
      <text font-family="Open Sans, sans-serif" font-size="24" fill="var(--red)" letter-spacing="5">
        <textPath href="#badgeArc" startOffset="50%" text-anchor="middle">MIX OF SPICES</textPath>
      </text>
    </svg>

    <h1 class="label-text brand-name">Zolv</h1>
    <p class="label-text product-name">Mouthfreshener</p>
    <p class="label-text origin"><span class="small">MADE IN </span><span class="big">USA</span></p>
    <p class="label-text ingredients">
      <span class="pair"><span>Saffron</span><span>Cardamom</span></span><br>
      <span class="pair"><span>Menthol</span><span>Catechu</span></span><br>
      Permited spices and falvors<br>
      Tree nuts
    </p>
    <p class="label-text net-weight">NET WT.150g</p>
  </section>
</main>
</body>
</html>
```